KTR Associates Business Card

I would like to have a business card designed that uses my current logo and colors. I am not looking for anything to "out there" but can have a little fun so that it stands out.

I have a boutique consulting firm that specializes in strategic planning, change management, leadership development and innovation.

Industry/Entity Type

Leadership

Contact Information for Business Card

Marta Holloway
President
marta@ktr-associates-mail.com
919-555-0143

```html
<!DOCTYPE html>
<html lang="en">
<head>
<meta charset="utf-8">
<title>KTR Associates Business Card</title>
<link rel="stylesheet" href="https://fonts.googleapis.com/css2?family=Libre+Baskerville&display=swap">
<style>
  :root {
    --backdrop: #c8c8c8;
    --card: #ffffff;
    --ink: #1e1e1e;
    --green-deep: #2f7a37;
    --green-mid: #5e9a3a;
    --green-lime: #b7c933;
    --title-green: #3f7d34;
    --shadow: rgba(0, 0, 0, 0.45);
  }
  * { margin: 0; padding: 0; box-sizing: border-box; }
  html, body {
    width: 1200px;
    height: 1044px;
    overflow: hidden;
    background: var(--backdrop);
    font-family: "Libre Baskerville", Georgia, serif;
  }
  .canvas { position: relative; width: 1200px; height: 1044px; }
  .card {
    position: absolute;
    background: var(--card);
    box-shadow: 4px 4px 5px var(--shadow);
    overflow: hidden;
  }
  .card--front { left: 56px; top: 49px; width: 837px; height: 484px; z-index: 2; }
  .card--back { left: 317px; top: 494px; width: 833px; height: 481px; z-index: 1; }

  .front-sweep { position: absolute; inset: 0; }
  .accent-rule {
    position: absolute;
    left: 56px; top: 32px;
    width: 2px; height: 420px;
    background: var(--green-deep);
  }
  .holder-name {
    position: absolute;
    left: 75px; top: 82px;
    font-size: 36px;
    color: var(--ink);
    letter-spacing: 0.3px;
  }
  .holder-title {
    position: absolute;
    left: 76px; top: 139px;
    font-size: 20px;
    color: var(--title-green);
    letter-spacing: 0.6px;
  }
  .contact-list { list-style: none; position: absolute; left: 79px; top: 296px; }
  .contact-item {
    display: flex;
    align-items: center;
    height: 48px;
    font-size: 22px;
    color: var(--ink);
  }
  .contact-icon { width: 30px; height: 30px; margin-right: 24px; flex: none; }
  .front-wordmark {
    position: absolute;
    right: 40px; top: 380px;
    font-size: 30px;
    color: #ffffff;
  }
  .back-wordmark {
    position: absolute;
    left: 0; right: 0; top: 200px;
    text-align: center;
    font-size: 66px;
    color: var(--ink);
  }
</style>
</head>
<body>
<main class="canvas">
  <section class="card card--front" aria-label="Business card front">
    <svg class="front-sweep" width="837" height="484" viewBox="0 0 837 484" aria-hidden="true">
      <defs>
        <linearGradient id="sweepFill" x1="0" y1="0" x2="0" y2="1">
          <stop offset="0" stop-color="var(--green-lime)"/>
          <stop offset="0.5" stop-color="var(--green-mid)"/>
          <stop offset="1" stop-color="var(--green-deep)"/>
        </linearGradient>
      </defs>
      <path d="M274 484 C 480 420, 700 330, 837 172 L 837 484 Z" fill="url(#sweepFill)"/>
      <path d="M262 484 C 470 424, 690 334, 837 182" fill="none" stroke="#ffffff" stroke-width="6" opacity="0.8"/>
    </svg>
    <div class="accent-rule"></div>
    <h1 class="holder-name">Marta Holloway</h1>
    <p class="holder-title">PRESIDENT</p>
    <ul class="contact-list">
      <li class="contact-item">
        <svg class="contact-icon" viewBox="0 0 30 30" aria-hidden="true">
          <rect x="2" y="7" width="26" height="17" fill="var(--green-mid)"/>
          <path d="M2 7 L15 17 L28 7" fill="none" stroke="#ffffff" stroke-width="2"/>
        </svg>
        marta@ktr-associates-mail.com
      </li>
      <li class="contact-item">
        <svg class="contact-icon" viewBox="0 0 30 30" aria-hidden="true">
          <path d="M8 4 L12 9 L10 12 C11 16 14 19 18 20 L21 18 L26 22 L23 26 C13 26 4 17 4 7 Z" fill="var(--green-mid)"/>
        </svg>
        919-555-0143
      </li>
      <li class="contact-item">
        <svg class="contact-icon" viewBox="0 0 30 30" aria-hidden="true">
          <circle cx="15" cy="15" r="13" fill="var(--green-mid)"/>
          <g fill="none" stroke="#ffffff" stroke-width="1.3">
            <ellipse cx="15" cy="15" rx="6" ry="13"/>
            <line x1="15" y1="2" x2="15" y2="28"/>
            <line x1="2" y1="15" x2="28" y2="15"/>
            <line x1="4" y1="9" x2="26" y2="9"/>
            <line x1="4" y1="21" x2="26" y2="21"/>
          </g>
        </svg>
        ktr-associates-mail.com
      </li>
    </ul>
    <p class="front-wordmark">KTR Associates</p>
  </section>

  <section class="card card--back" aria-label="Business card back">
    <p class="back-wordmark">KTR Associates</p>
  </section>
</main>
</body>
</html>
```